THE POINT AT MAPLE SWALE HUDSON RIVER WATERFRONT LAND

crisp clear business cards on wood stock or thick paper with large font with a river otter logo, PERSONAL INFO ON ONE SIDE, PROJECT INFO ON THE OTHER SIDE
Updates

I don’t have a logo. Just thought that a photo of a river otter would look appealing.

Target Market(s)

Buyers and realtors

Industry/Entity Type

Real Estate Development

Contact Information for Business Card

MARTIN OSGOOD
518-730-4862 (Call or Text)
STONE HAVEN LLC PRINCIPAL

MOSHAVENRD@TARNMAIL.COM

Font styles to use
Sans Serif

Colors
fbfdfe
0792cd
00a990
fbed22
ec1f27

Requirements
Must have
• LARGE FONT, ROUNDED EDGES,
Nice to have
• ON THE BACK SIDE :
• THE POINT AT MAPLE SWALE
• HUDSON RIVER WATERFRONT LAND
• 2 TO 67 ACRES---READY TO BUILD
• PRICED TO SELL!

```html
<!DOCTYPE html>
<html lang="en">
<head>
<meta charset="utf-8">
<title>Stone Haven LLC – Business Cards</title>
<link rel="stylesheet" href="https://fonts.googleapis.com/css2?family=Oswald:wght@700&family=Lato:wght@400&family=Arimo:wght@400&display=swap">
<style>
  :root {
    --backdrop: #d9d9db;
    --paper: #fbfdfe;
    --river-blue: #0792cd;
    --river-teal: #00a990;
    --ink: #1d1d1d;
    --white: #ffffff;
    --card-radius: 30px;
  }
  * { box-sizing: border-box; margin: 0; padding: 0; }
  html, body {
    width: 1200px;
    height: 900px;
    overflow: hidden;
    background: var(--backdrop);
  }
  .stage {
    position: relative;
    width: 1200px;
    height: 900px;
  }
  .card {
    position: absolute;
    width: 540px;
    height: 310px;
    border-radius: var(--card-radius);
    box-shadow: 0 6px 18px rgba(0, 0, 0, 0.14);
    display: flex;
    flex-direction: column;
    align-items: center;
    justify-content: center;
    text-align: center;
  }

  /* Project side */
  .card--project {
    left: 90px;
    top: 120px;
    background: var(--paper);
  }
  .card--project .company-name {
    font-family: "Oswald", sans-serif;
    font-weight: 700;
    font-size: 60px;
    line-height: 1;
    letter-spacing: 0.5px;
    color: var(--river-teal);
    margin-bottom: 34px;
  }
  .project-info {
    list-style: none;
    font-family: "Arimo", sans-serif;
    font-size: 13px;
    line-height: 1.3;
    color: var(--ink);
    text-transform: uppercase;
    letter-spacing: 0.3px;
  }

  /* Personal side */
  .card--personal {
    left: 570px;
    top: 470px;
    background: linear-gradient(160deg, var(--river-teal) 0%, #04a0b0 50%, var(--river-blue) 100%);
    color: var(--white);
  }
  .card--personal .company-name {
    font-family: "Oswald", sans-serif;
    font-weight: 700;
    font-size: 56px;
    line-height: 1;
    letter-spacing: 0.5px;
    color: var(--white);
    margin-bottom: 22px;
  }
  .person-name {
    font-family: "Lato", sans-serif;
    font-size: 23px;
    letter-spacing: 1px;
    line-height: 1.1;
  }
  .person-role {
    font-family: "Lato", sans-serif;
    font-size: 12px;
    letter-spacing: 1.5px;
    margin-top: 2px;
  }
  .divider {
    width: 250px;
    height: 1px;
    background: rgba(255, 255, 255, 0.85);
    margin: 12px 0 10px;
  }
  .contact-phone {
    font-family: "Lato", sans-serif;
    font-size: 20px;
    line-height: 1.2;
  }
  .contact-email {
    font-family: "Lato", sans-serif;
    font-size: 14px;
    letter-spacing: 0.5px;
    margin-top: 3px;
  }
</style>
</head>
<body>
  <main class="stage">
    <section class="card card--project" aria-label="Project side">
      <h1 class="company-name">STONE HAVEN LLC</h1>
      <ul class="project-info">
        <li>The Point at Maple Swale</li>
        <li>Hudson River Waterfront Land</li>
        <li>2 to 67 Acres---Ready to Build | Priced to Sell!</li>
      </ul>
    </section>

    <section class="card card--personal" aria-label="Personal side">
      <h2 class="company-name">STONE HAVEN LLC</h2>
      <p class="person-name">MARTIN OSGOOD</p>
      <p class="person-role">PRINCIPAL</p>
      <div class="divider"></div>
      <p class="contact-phone">Call or Text : 518-730-4862</p>
      <p class="contact-email">MOSHAVENRD@TARNMAIL.COM</p>
    </section>
  </main>
</body>
</html>
```